Modern Label for Loose Tea pouches on 4.5x6 Label

We need a new label for our teas that is very simple in design, but stylish and modern. This will be used to print labels for our loose tea pouches. The label will be at max 4.5x6 inches in size. There should be a place for the tea name, description, ingredients, and size that is changeable.
Preferably an AI file that allows me to setup variables to change the above items. There will also need to be our logo which is supplied, and our address on the label.
Address:
Tallowby Teas
846 Lower Maple Lane
Elmbrook, VT 05999
Target Market(s)
Tea Lovers
Requirements
Must have
- Adobe Illustrator file with variables setup for replacement of tea name, description, ingredients, and size (weights 2oz, 4oz, 8oz, 1lb)

```html
<!DOCTYPE html>
<html lang="en">
<head>
<meta charset="utf-8">
<title>Tallowby Teas – Loose Tea Labels</title>
<link rel="stylesheet" href="https://fonts.googleapis.com/css2?family=Jost:wght@400;500;600&display=swap">
<style>
  :root {
    --page: #eeeeec;
    --paper: #f7f6f3;
    --leaf-light: #9fd36a;
    --leaf-dark: #3f8a2c;
    --brand-pink: #d7489a;
    --chamomile: #a0642a;
    --chamomile-band: rgba(123,74,29,.9);
    --chamomile-text: #f3b15a;
    --earl: #3a3a3a;
    --earl-band: rgba(43,43,43,.9);
    --earl-text: #9a9a9a;
    --earl-desc: #c4c4c4;
    --green: #4f8a3a;
    --green-band: rgba(61,122,45,.94);
    --green-text: #c7e36a;
    --white: #ffffff;
  }
  * { box-sizing: border-box; margin: 0; padding: 0; }
  html, body { width: 1200px; height: 849px; overflow: hidden; }
  body {
    background: var(--page);
    font-family: "Jost", Arial, sans-serif;
    display: flex;
    align-items: center;
    justify-content: center;
    gap: 40px;
  }
  .label {
    position: relative;
    width: 340px;
    height: 500px;
    background: var(--paper);
    overflow: hidden;
    box-shadow: 0 2px 10px rgba(0,0,0,.12);
  }
  .label__leaves {
    position: absolute;
    top: 0; left: 0;
    width: 100%; height: 150px;
    background:
      radial-gradient(ellipse 90px 70px at 0% 10%, var(--leaf-dark), transparent 70%),
      radial-gradient(ellipse 70px 60px at 30% 0%, var(--leaf-light), transparent 70%),
      radial-gradient(ellipse 90px 80px at 100% 15%, var(--leaf-dark), transparent 70%),
      radial-gradient(ellipse 60px 90px at 100% 70%, var(--leaf-light), transparent 70%);
  }
  .brand {
    position: absolute;
    top: 62px; left: 0; width: 100%;
    display: flex;
    align-items: center;
    justify-content: center;
    gap: 9px;
  }
  .brand__dot {
    flex: none;
    width: 16px; height: 16px;
    border-radius: 50%;
    background: var(--brand-pink);
  }
  .brand__name {
    font-size: 25px;
    font-weight: 500;
    letter-spacing: 1.5px;
    text-transform: uppercase;
    white-space: nowrap;
    color: var(--brand-pink);
  }
  .label__photo {
    position: absolute;
    top: 150px; left: 0;
    width: 100%; height: 240px;
  }
  .label--chamomile .label__photo { background: linear-gradient(160deg, #d9a24a, #8a5a2a 55%, #c9b48a); }
  .label--earl .label__photo { background: linear-gradient(160deg, #8a6a4a, #3a2418 55%, #5a3a2a); }
  .label--green .label__photo { background: linear-gradient(160deg, #f2efe8, #a97a52 50%, #6a7a4a); }
  .title-band {
    position: absolute;
    top: 225px; left: 0; width: 100%;
    padding: 6px 10px 5px;
    text-align: center;
  }
  .title-band__name {
    font-size: 30px;
    font-weight: 500;
    letter-spacing: 1px;
    text-transform: uppercase;
    color: var(--white);
    line-height: 1.1;
    white-space: nowrap;
  }
  .title-band__desc {
    font-size: 10px;
    line-height: 1.3;
    white-space: nowrap;
  }
  .label--chamomile .title-band { background: var(--chamomile-band); }
  .label--chamomile .title-band__desc { color: var(--chamomile-text); }
  .label--earl .title-band { background: var(--earl-band); }
  .label--earl .title-band__desc { color: var(--earl-desc); }
  .label--green .title-band { background: var(--green-band); }
  .label--green .title-band__desc { color: var(--green-text); }
  .label__footer {
    position: absolute;
    top: 390px; left: 0;
    width: 100%; height: 110px;
    text-align: center;
    padding: 22px 8px 0;
  }
  .label--chamomile .label__footer { background: var(--chamomile); color: var(--chamomile-text); }
  .label--earl .label__footer { background: var(--earl); color: var(--earl-text); }
  .label--green .label__footer { background: var(--green); color: var(--green-text); }
  .label__size { font-size: 18px; font-weight: 500; color: var(--white); }
  .label--earl .label__size { color: var(--earl-desc); }
  .label__address { margin-top: 16px; font-size: 9.5px; letter-spacing: .2px; white-space: nowrap; }
</style>
</head>
<body>
  <article class="label label--chamomile">
    <div class="label__leaves" role="img" aria-label="Fresh green tea leaves framing the top corners"></div>
    <div class="brand"><span class="brand__dot"></span><span class="brand__name">Tallowby Teas</span></div>
    <div class="label__photo" role="img" aria-label="Dried chamomile flowers in a wooden scoop beside a glass cup of tea"></div>
    <div class="title-band">
      <h2 class="title-band__name">Chamomile Tea</h2>
      <p class="title-band__desc">Sooth your weary soul with our Rejuvinative Blend</p>
    </div>
    <footer class="label__footer">
      <p class="label__size">2oz</p>
      <p class="label__address">Address: Tallowby Teas | 846 Lower Maple Lane | Elmbrook, VT 05999</p>
    </footer>
  </article>

  <article class="label label--earl">
    <div class="label__leaves" role="img" aria-label="Fresh green tea leaves framing the top corners"></div>
    <div class="brand"><span class="brand__dot"></span><span class="brand__name">Tallowby Teas</span></div>
    <div class="label__photo" role="img" aria-label="Loose black Earl Grey tea leaves in a wooden bowl"></div>
    <div class="title-band">
      <h2 class="title-band__name">Earl Grey</h2>
      <p class="title-band__desc">A Masterful blend using only the finest Earl grey selection</p>
    </div>
    <footer class="label__footer">
      <p class="label__size">2oz</p>
      <p class="label__address">Address: Tallowby Teas | 846 Lower Maple Lane | Elmbrook, VT 05999</p>
    </footer>
  </article>

  <article class="label label--green">
    <div class="label__leaves" role="img" aria-label="Fresh green tea leaves framing the top corners"></div>
    <div class="brand"><span class="brand__dot"></span><span class="brand__name">Tallowby Teas</span></div>
    <div class="label__photo" role="img" aria-label="Rolled green tea leaves in a wooden bowl"></div>
    <div class="title-band">
      <h2 class="title-band__name">Green Tea</h2>
      <p class="title-band__desc">For Health and Rejuvination through our unique aromatic blend</p>
    </div>
    <footer class="label__footer">
      <p class="label__size">2oz</p>
      <p class="label__address">Address: Tallowby Teas | 846 Lower Maple Lane | Elmbrook, VT 05999</p>
    </footer>
  </article>
</body>
</html>
```